Cleaning services Business Card Design

I need a business card design for my Cleaning business. I would like perhaps emphasis on the company name, Muddle to Marvel. Maybe the Muddle would to dirty and the marvel would have sprinkles.

Industry/Entity Type

Business

Contact Information for Business Card

Muddle to Marvel Cleaning Services, Teodoro Perlas, Industrial, Commercial, & Residential 418-635-0247

```html
<!DOCTYPE html>
<html lang="en">
<head>
<meta charset="UTF-8">
<title>Muddle to Marvel Cleaning Services – Business Card</title>
<link href="https://fonts.googleapis.com/css2?family=Open+Sans:wght@400;600;700&display=swap" rel="stylesheet">
<style>
  :root {
    --backdrop: #ecebe8;
    --card: #ffffff;
    --teal: #1fb8c7;
    --navy: #1c3a50;
    --white: #ffffff;
  }
  * { margin: 0; padding: 0; box-sizing: border-box; }
  html, body {
    width: 1200px;
    height: 1000px;
    overflow: hidden;
    background: var(--backdrop);
    font-family: "Open Sans", Arial, sans-serif;
  }
  .business-card {
    position: absolute;
    left: 100px;
    top: 201px;
    width: 1000px;
    height: 598px;
    background: var(--card);
    box-shadow: 0 6px 18px rgba(0,0,0,0.18);
  }
  .brand {
    position: absolute;
    top: 70px;
    left: 0;
    width: 100%;
    text-align: center;
    color: var(--teal);
    font-weight: 700;
  }
  .brand-name {
    font-size: 64px;
    line-height: 1.1;
  }
  .brand-tagline {
    font-size: 30px;
    letter-spacing: 5px;
    margin-top: 6px;
  }
  .services-band {
    position: absolute;
    top: 293px;
    left: 0;
    width: 100%;
    height: 34px;
    background: var(--teal);
    color: var(--white);
    font-size: 25px;
    line-height: 34px;
  }
  .services-band span {
    position: absolute;
    top: 0;
    transform: translateX(-50%);
    white-space: nowrap;
  }
  .photo-strip {
    position: absolute;
    top: 327px;
    left: 0;
    width: 100%;
    height: 134px;
    display: flex;
  }
  .photo { height: 100%; }
  .photo-industrial {
    width: 335px;
    background: linear-gradient(180deg, #9fc3d6 0%, #dfe8ee 55%, #c7d3da 100%);
  }
  .photo-commercial {
    width: 330px;
    background: linear-gradient(180deg, #d9dde0 0%, #f1f2f2 50%, #8a8f93 100%);
  }
  .photo-residential {
    width: 335px;
    background: linear-gradient(90deg, #7a5a3c 0%, #c59a6a 45%, #e9e3d6 100%);
  }
  .strip-rule {
    position: absolute;
    top: 461px;
    left: 0;
    width: 100%;
    height: 5px;
    background: var(--teal);
  }
  .contact {
    position: absolute;
    top: 512px;
    left: 0;
    width: 100%;
    color: var(--navy);
  }
  .contact-name {
    position: absolute;
    left: 206px;
    font-size: 39px;
    font-weight: 600;
    white-space: nowrap;
  }
  .contact-phone {
    position: absolute;
    left: 507px;
    top: 8px;
    display: flex;
    align-items: center;
    gap: 10px;
    white-space: nowrap;
  }
  .call-label { font-size: 29px; font-weight: 600; }
  .phone-icon { width: 24px; height: 24px; }
  .phone-number { font-size: 26px; font-weight: 400; }
</style>
</head>
<body>
  <div class="business-card">
    <div class="brand">
      <div class="brand-name">Muddle to Marvel</div>
      <div class="brand-tagline">CLEANING SERVICES</div>
    </div>

    <div class="services-band">
      <span style="left:183px">Industrial</span>
      <span style="left:333px">-</span>
      <span style="left:501px">Commercial</span>
      <span style="left:666px">-</span>
      <span style="left:813px">Residential</span>
    </div>

    <div class="photo-strip">
      <div class="photo photo-industrial" role="img" aria-label="Bright warehouse interior with a yellow forklift"></div>
      <div class="photo photo-commercial" role="img" aria-label="Modern office lounge with grey sofas and city view"></div>
      <div class="photo photo-residential" role="img" aria-label="Home interior with fireplace, dining table and wooden floor"></div>
    </div>
    <div class="strip-rule"></div>

    <div class="contact">
      <div class="contact-name">Teodoro Perlas</div>
      <div class="contact-phone">
        <span class="call-label">Call us</span>
        <svg class="phone-icon" viewBox="0 0 24 24" aria-hidden="true">
          <path fill="#1c3a50" d="M6.6 10.8c1.4 2.8 3.8 5.1 6.6 6.6l2.2-2.2c.3-.3.7-.4 1-.2 1.1.4 2.3.6 3.6.6.6 0 1 .4 1 1V20c0 .6-.4 1-1 1C10.6 21 3 13.4 3 4c0-.6.4-1 1-1h3.5c.6 0 1 .4 1 1 0 1.3.2 2.5.6 3.6.1.3 0 .7-.2 1z"/>
        </svg>
        <span class="phone-number">418-635-0247</span>
      </div>
    </div>
  </div>
</body>
</html>
```